Brightmoor Ridge College Viewbook 2019

Create a small brochure booklet to hand out as marketing materials for student Outreach & Recruitment. Need to reach a younger audience, mostly high school age within our local region and district.

Target Market(s)

Prospective students

Industry/Entity Type

College

Font styles to use
Serif

Colors

Designer to choose colors to be used in the design.

Requirements
Must have
• Try to recruit region's students to Brightmoor Ridge College.
Nice to have
• cool design, simple brochure that pops

```html
<!DOCTYPE html>
<html lang="en">
<head>
<meta charset="utf-8">
<title>Brightmoor Ridge College Viewbook 2019</title>
<link rel="stylesheet" href="https://fonts.googleapis.com/css2?family=Oswald:wght@500;700&family=Montserrat:wght@600;700;800&family=Open+Sans:wght@400;600&display=swap">
<style>
  :root{
    --green:#3f9a3b;
    --green-dark:#2b7a2e;
    --green-light:#8cc63f;
    --ink:#2f2f2f;
    --muted:#6b6b6b;
    --paper:#ffffff;
    --paper-grey:#eeeeee;
    --stage:#f4f4f4;
    --rule:#cfcfcf;
  }
  *{box-sizing:border-box;margin:0;padding:0}
  html,body{width:1200px;height:4096px;overflow:hidden}
  body{background:var(--stage);font-family:"Open Sans",Arial,sans-serif;color:var(--ink);
    display:flex;flex-direction:column;align-items:center;justify-content:center;gap:180px}
  .spread{position:relative;width:1100px;height:900px;display:flex;box-shadow:0 6px 24px rgba(0,0,0,.12)}
  .page{position:relative;width:550px;height:900px;overflow:hidden;
    background:linear-gradient(160deg,#fafafa 0%,var(--paper-grey) 100%)}
  .page + .page{border-left:1px solid #dcdcdc}
  .shapes{position:absolute;inset:0;width:100%;height:100%}
  .photo{position:absolute}
  .photo-keyboard{left:0;top:150px;width:550px;height:420px;
    background:linear-gradient(200deg,#d9dde2 0%,#6f7f95 45%,#2d3b52 100%)}
  .photo-students{left:0;top:170px;width:550px;height:440px;
    background:linear-gradient(180deg,#c8ccc4 0%,#9aa38e 40%,#7b6f64 75%,#4b4a52 100%)}
  .photo-workshop{left:40px;top:330px;width:470px;height:300px;
    background:linear-gradient(120deg,#2a2a2e 0%,#5a3a3a 45%,#b3262b 70%,#3a3a40 100%)}
  .photo-transfer{left:40px;top:640px;width:150px;height:110px;
    background:linear-gradient(180deg,#c9d2cf,#6f7f7a)}
  .photo-walking{left:280px;top:560px;width:240px;height:220px;
    background:linear-gradient(180deg,#e8ece6 0%,#b6bcb0 50%,#6b5f66 100%)}
  .brand{position:absolute;display:flex;align-items:center;gap:10px;
    font-family:"Montserrat",Arial,sans-serif;font-weight:700;color:var(--green-dark);font-size:15px;letter-spacing:.5px;white-space:nowrap}
  .brand-dot{width:22px;height:22px;border-radius:50%;background:var(--green)}
  .address{position:absolute;left:96px;top:660px;font-size:12px;line-height:1.55;color:var(--ink);font-weight:600;letter-spacing:.4px}
  .headline{position:absolute;left:0;width:100%;text-align:center;font-family:"Oswald",Arial,sans-serif;font-weight:700;line-height:1}
  .headline-main{top:640px;font-size:60px;color:var(--green-dark)}
  .headline-sub{top:708px;font-size:54px;color:var(--green-light)}
  .web{position:absolute;left:0;width:100%;text-align:center;top:782px;font-family:"Montserrat",Arial,sans-serif;font-weight:600;font-size:15px;color:var(--muted);letter-spacing:1px}
  .body-copy{position:absolute;left:40px;width:470px;font-size:12.5px;line-height:1.55;color:var(--ink)}
  .section-title{position:absolute;left:40px;width:470px;font-family:"Montserrat",Arial,sans-serif;font-weight:800;font-size:16px;line-height:1.25;color:var(--green)}
  .features{position:absolute;left:30px;top:30px;width:490px;height:170px;background:var(--green);padding:22px 22px;
    display:grid;grid-template-columns:1fr 1fr;column-gap:16px;align-content:start}
  .features ul{list-style:none}
  .features li{display:flex;align-items:center;gap:7px;font-family:"Montserrat",Arial,sans-serif;font-weight:600;font-size:10.5px;color:#fff;margin-bottom:10px}
  .tick{width:12px;height:12px;flex:none}
  .score-title{position:absolute;left:30px;top:228px;font-family:"Montserrat",Arial,sans-serif;font-weight:800;font-size:17px;line-height:1.25;color:var(--green)}
  .chart{position:absolute;top:300px;width:235px;height:200px;background:#fff;border:1px solid var(--rule)}
  .chart-left{left:30px}
  .chart-right{left:285px}
  .chart-label{position:absolute;left:14px;top:10px;font-family:"Montserrat",Arial,sans-serif;font-weight:700;font-size:13px;color:var(--green)}
  .rate-title{position:absolute;left:40px;top:520px;width:220px;font-family:"Montserrat",Arial,sans-serif;font-weight:800;font-size:15px;color:var(--green);border-bottom:3px solid var(--green);padding-bottom:6px}
  .recruit{position:absolute;left:280px;top:520px;width:240px;font-family:"Montserrat",Arial,sans-serif;font-weight:700;font-size:10.5px;line-height:1.3;color:var(--ink)}
  .visit{position:absolute;left:30px;top:790px;width:240px;height:80px;background:var(--green);color:#fff;
    font-family:"Montserrat",Arial,sans-serif;font-weight:700;line-height:1.2;padding:14px 14px}
  .visit-lead{display:block;font-size:20px}
  .visit-url{display:block;font-size:13px;white-space:nowrap;margin-top:4px}
</style>
</head>
<body>

<section class="spread spread-outside">
  <div class="page back-cover">
    <div class="photo photo-keyboard" role="img" aria-label="Close-up photograph of a laptop keyboard in cool blue light"></div>
    <svg class="shapes" viewBox="0 0 550 900" aria-hidden="true">
      <polygon points="0,0 550,0 550,60 0,150" fill="#f6f6f6"/>
      <polygon points="0,110 550,30 550,70 0,160" fill="var(--green)"/>
      <polygon points="300,0 550,0 550,40" fill="var(--green-light)"/>
      <polygon points="0,470 0,580 260,580" fill="var(--green)"/>
      <polygon points="0,520 0,580 140,580" fill="var(--green-light)"/>
      <polygon points="550,430 550,580 330,580" fill="var(--green-dark)" opacity=".9"/>
      <polygon points="0,580 550,580 550,900 0,900" fill="#f1f1f1"/>
      <polygon points="0,760 220,900 0,900" fill="#e4e4e4"/>
      <polygon points="330,900 550,720 550,900" fill="#e6e6e6"/>
    </svg>
    <div class="brand" style="left:60px;top:615px"><span class="brand-dot"></span>BRIGHTMOOR RIDGE COLLEGE</div>
    <div class="address">1420 LARKSPUR HILL RD<br>MARLOW, CA 95210<br><br>408.555.0142</div>
  </div>

  <div class="page front-cover">
    <svg class="shapes" viewBox="0 0 550 900" aria-hidden="true">
      <rect width="550" height="110" fill="#ffffff"/>
      <polygon points="0,30 550,110 550,200 0,120" fill="var(--green)"/>
      <polygon points="0,90 260,130 0,180" fill="var(--green-light)"/>
    </svg>
    <div class="photo photo-students" role="img" aria-label="Photograph of smiling students gathered around a laptop"></div>
    <svg class="shapes" viewBox="0 0 550 900" aria-hidden="true">
      <polygon points="0,500 0,610 200,610" fill="var(--green)"/>
      <polygon points="550,520 550,610 360,610" fill="var(--green-light)"/>
      <polygon points="0,610 550,610 550,900 0,900" fill="#f1f1f1"/>
      <polygon points="0,820 160,900 0,900" fill="#e3e3e3"/>
      <polygon points="400,900 550,790 550,900" fill="#e3e3e3"/>
    </svg>
    <div class="brand" style="left:150px;top:42px"><span class="brand-dot"></span>BRIGHTMOOR RIDGE COLLEGE</div>
    <div class="headline headline-main">TRASNFER FASTER</div>
    <div class="headline headline-sub">TRANSFER SMATER</div>
    <div class="web">www.brightmoorridge.edu</div>
  </div>
</section>

<section class="spread spread-inside">
  <div class="page inside-left" style="background:#fff">
    <p class="body-copy" style="top:34px">At Brightmoor Ridge College we believe every learner deserves a clear path forward. Our faculty, counselors and peers work together so you can explore, grow and transfer with confidence to the university of your choice.</p>
    <h2 class="section-title" style="top:150px">BRIGHTMOOR RIDGE COLLEGE<br>RECOGNIZED AS A STRONG WORKFORCE STAR</h2>
    <p class="body-copy" style="top:205px">Brightmoor Ridge College was honored for programs that lead students to good jobs and higher wages. Hands-on training in our labs prepares you for careers in advanced manufacturing, health, technology and more.</p>
    <div class="photo photo-workshop" role="img" aria-label="Photograph of students working together in a technical workshop"></div>
    <svg class="shapes" viewBox="0 0 550 900" aria-hidden="true">
      <polygon points="0,690 550,620 550,900 0,900" fill="#f0f0f0"/>
      <polygon points="0,690 260,657 0,750" fill="var(--green)"/>
    </svg>
    <p class="body-copy" style="top:790px">To facilitate each student's educational journey, we offer counseling, tutoring and a wide range of support services close to home.</p>
  </div>

  <div class="page inside-right" style="background:#fff">
    <div class="features">
      <ul>
        <li><svg class="tick" viewBox="0 0 12 12"><path d="M1 6l3.5 3.5L11 2" stroke="#fff" stroke-width="2" fill="none"/></svg>OUTSTANDING ACADEMICS</li>
        <li><svg class="tick" viewBox="0 0 12 12"><path d="M1 6l3.5 3.5L11 2" stroke="#fff" stroke-width="2" fill="none"/></svg>BRILLIANT FACULTY</li>
        <li><svg class="tick" viewBox="0 0 12 12"><path d="M1 6l3.5 3.5L11 2" stroke="#fff" stroke-width="2" fill="none"/></svg>EXCELLENT TRANSFER RATE</li>
        <li><svg class="tick" viewBox="0 0 12 12"><path d="M1 6l3.5 3.5L11 2" stroke="#fff" stroke-width="2" fill="none"/></svg>THRIVING CAMPUS LIFE</li>
      </ul>
      <ul>
        <li><svg class="tick" viewBox="0 0 12 12"><path d="M1 6l3.5 3.5L11 2" stroke="#fff" stroke-width="2" fill="none"/></svg>INTERNATIONAL STUDENT PROGRAM</li>
        <li><svg class="tick" viewBox="0 0 12 12"><path d="M1 6l3.5 3.5L11 2" stroke="#fff" stroke-width="2" fill="none"/></svg>ATHLETIC TEAMS</li>
        <li><svg class="tick" viewBox="0 0 12 12"><path d="M1 6l3.5 3.5L11 2" stroke="#fff" stroke-width="2" fill="none"/></svg>SUPPORTIVE COMMUNITY</li>
        <li><svg class="tick" viewBox="0 0 12 12"><path d="M1 6l3.5 3.5L11 2" stroke="#fff" stroke-width="2" fill="none"/></svg>STUDY ABROAD</li>
        <li><svg class="tick" viewBox="0 0 12 12"><path d="M1 6l3.5 3.5L11 2" stroke="#fff" stroke-width="2" fill="none"/></svg>HIGH FINANCIAL AID</li>
      </ul>
    </div>
    <h3 class="score-title">BRIGHTMOOR RIDGE COLLEGE<br>STUDENT SUCCESS SCORE CARD</h3>

    <div class="chart chart-left">
      <span class="chart-label">+ 31.6%</span>
      <svg class="shapes" viewBox="0 0 235 200" aria-hidden="true">
        <line x1="20" y1="175" x2="215" y2="175" stroke="#bbb"/>
        <rect x="28" y="70" width="18" height="105" fill="var(--green)"/>
        <rect x="58" y="90" width="18" height="85" fill="#b5b5b5"/>
        <rect x="88" y="80" width="18" height="95" fill="#b5b5b5"/>
        <rect x="118" y="95" width="18" height="80" fill="#b5b5b5"/>
        <rect x="148" y="85" width="18" height="90" fill="#b5b5b5"/>
        <rect x="178" y="75" width="18" height="100" fill="#b5b5b5"/>
      </svg>
    </div>
    <div class="chart chart-right">
      <svg class="shapes" viewBox="0 0 235 200" aria-hidden="true">
        <line x1="20" y1="175" x2="215" y2="175" stroke="#bbb"/>
        <rect x="30" y="60" width="20" height="115" fill="#b5b5b5"/>
        <rect x="64" y="70" width="20" height="105" fill="#b5b5b5"/>
        <rect x="98" y="55" width="20" height="120" fill="#b5b5b5"/>
        <rect x="132" y="65" width="20" height="110" fill="#b5b5b5"/>
        <rect x="166" y="58" width="20" height="117" fill="#b5b5b5"/>
      </svg>
    </div>

    <h3 class="rate-title">SIX YEAR TRANSFER RATE</h3>
    <div class="photo photo-transfer" role="img" aria-label="Photograph of students on campus"></div>
    <p class="recruit">RECRUIT REGION'S STUDENTS TO<br>BRIGHTMOOR RIDGE COLLEGE</p>
    <div class="photo photo-walking" role="img" aria-label="Photograph of students walking across campus"></div>
    <div class="visit"><span class="visit-lead">Visit us at</span><span class="visit-url">www.brightmoorridge.edu</span></div>
  </div>
</section>

</body>
</html>
```